Bottle label - mead

We need a bottle label (logo) design for a new mead product as part of our Whistling Pines Brewing Co. brand. There are two parts to this project. We need a logo design for the mead product which is placed on the front of a bottle wrap that has additional information on the back of the label.
Whistling Pines Brewing Co. is a New Zealand craft beer brand that is expanding its product range to a new mead product.
Mead is an ancient honey based alcoholic beverage ranging between beer and wine. Mead has many different sub-styles. Our strategy is to position mead primarily to the beer drinkers.
Note: Most meads in New Zealand today are packaged and promoted as a “honey wine”. We want to break away from this positioning. We will be using bottles that are much more in tune with the beer industry.
Label dimensions: Approximately 80mm high and 150mm wide for the entire label which wraps around the bottle. The main graphic that will be visible on the front is approximately 50mm wide.
Target Market(s)
Our strategy is to position mead primarily to the beer drinkers.
Target age group 25 – 50. We want the label to:
• Represent the brand Whistling Pines Brewing Co.
• Establish a recognizable “Mead” product offering within our brand
• Be classy and playful, highlight “mead” (not honey) as the product
• Sit comfortably on a shelf amongst beer labels and not look out of place but be distinguished from beer (and greatly distinguished from wine)
• Flexible - be a master template for our complete mead range where styles and flavor names and graphics can be added in as new products are commercialized
Requirements
Must have
- Must have the following elements on the front of the label:
- Existing Whistling Pines Brewing Co corporate logo
- To be designed: Whistling Pines Mead logo
- alcohol content: e.g. 10.5%
On the back of the bottle wrapper we need room for
- the story (about the product, about us)
- handcrafted in Auckland, New Zealand
- This product contains approximately 3 standard drinks
- website address (www.examplesocial.com/WhistlingPines)
- barcode
Should not have
- any association with the traditional honey wine. We don't want images of bees, honey pots, bears.

```html
<!DOCTYPE html>
<html lang="en">
<head>
<meta charset="utf-8">
<title>Whistling Pines Mead – Bottle Wrap Label</title>
<link href="https://fonts.googleapis.com/css2?family=Alfa+Slab+One&family=Oswald:wght@300&family=Lato:wght@300;400;700&family=Gelasio&display=swap" rel="stylesheet">
<style>
  :root {
    --label-gold: #b5891f;
    --ink: #1a1409;
    --band: #3b2f14;
    --page: #ffffff;
  }
  * { margin: 0; padding: 0; box-sizing: border-box; }
  html, body {
    width: 1041px; height: 1200px; overflow: hidden;
    background: var(--page);
  }
  .label {
    position: absolute; left: 20px; top: 333px;
    width: 1000px; height: 533px;
    background: var(--label-gold);
    color: var(--ink);
    overflow: hidden;
  }
  .bone-band {
    position: absolute; left: 0; width: 100%; height: 56px;
    background: linear-gradient(to bottom, #2a2110, var(--band));
    opacity: .85;
  }
  .bone-band--top { top: 0; }
  .bone-band--bottom { bottom: 0; }
  .brand-mark {
    position: absolute; left: 196px; top: 8px; width: 130px; height: 70px;
    background: var(--label-gold);
    display: flex; align-items: center; justify-content: center;
    font-family: "Alfa Slab One", serif; font-size: 14px; line-height: 1.1;
    text-align: center;
  }
  .front-title {
    position: absolute; left: 164px; top: 146px; width: 200px;
    text-align: center;
  }
  .front-title__name {
    font-family: "Alfa Slab One", serif; font-size: 25px; line-height: 1.05;
    letter-spacing: .5px; text-transform: uppercase;
  }
  .front-title__name--large { font-size: 30px; }
  .front-title__product {
    font-family: "Oswald", sans-serif; font-weight: 300;
    font-size: 40px; line-height: 1; letter-spacing: 1px;
  }
  .mead-emblem {
    position: absolute; left: 181px; top: 248px; width: 165px; height: 218px;
    border-radius: 48% 48% 42% 42%;
    background: radial-gradient(circle at 50% 45%, var(--band), var(--ink));
  }
  .abv {
    position: absolute; left: 371px; top: 402px;
    font-family: "Lato", sans-serif; font-weight: 300; font-size: 13px; line-height: 1.35;
  }
  .back-panel {
    position: absolute; left: 714px; top: 62px; width: 250px;
    text-align: center;
  }
  .back-mark {
    margin: 0 auto; width: 90px; height: 64px;
    display: flex; align-items: center; justify-content: center;
    font-family: "Alfa Slab One", serif; font-size: 11px; line-height: 1.1;
  }
  .origin {
    margin-top: 18px;
    font-family: "Alfa Slab One", serif; font-size: 15px; font-weight: 400; line-height: 1.3;
    text-transform: uppercase; letter-spacing: .3px;
  }
  .divider {
    width: 30px; height: 0; margin: 12px auto 10px;
    border: 0; border-top: 2px solid var(--ink);
  }
  .story {
    font-family: "Lato", sans-serif; font-size: 15.5px; line-height: 1.3;
  }
  .story__tagline { font-weight: 700; }
  .back-notes {
    position: absolute; left: 726px; top: 350px; width: 180px;
    font-family: "Gelasio", serif; font-size: 10px; line-height: 1.3;
  }
  .drinks-note { display: flex; align-items: center; gap: 6px; }
  .drinks-note__text { width: 92px; }
  .drinks-note__icons { display: flex; gap: 2px; }
  .drinks-note__icons span {
    width: 10px; height: 12px; border-radius: 50%; background: var(--band);
  }
  .web-link {
    margin-top: 12px; margin-left: -4px;
    display: flex; align-items: center; gap: 5px; white-space: nowrap;
  }
  .web-link__dot {
    flex-shrink: 0;
    width: 11px; height: 11px; border-radius: 50%; background: var(--ink);
  }
</style>
</head>
<body>
  <main class="label">
    <div class="bone-band bone-band--top" role="img" aria-label="Repeating row of black bones along the top edge"></div>

    <div class="brand-mark">Whistling Pines<br>Brewing Co.</div>

    <section class="front-title">
      <div class="front-title__name">Whistling</div>
      <div class="front-title__name front-title__name--large">Pines</div>
      <div class="front-title__product">MEAD</div>
    </section>

    <div class="mead-emblem" role="img" aria-label="Black emblem built from bones and honeycomb hexagons"></div>

    <p class="abv">10.5%<br>ALC<br>VOL</p>

    <section class="back-panel">
      <div class="back-mark">Whistling Pines<br>Brewing Co.</div>
      <h2 class="origin">Handcrafted in<br>Auckland<br>New Zealand</h2>
      <hr class="divider">
      <p class="story">Whistling Pines Brewing is a new Craft beer label in New Zealand set out to produce a range of high-quality craft beers reflecting true kiwi culture.</p>
      <p class="story story__tagline">Fine craft beers for Everyone!</p>
    </section>

    <div class="back-notes">
      <div class="drinks-note">
        <span class="drinks-note__text">This product contains approximately 3 standard drinks</span>
        <span class="drinks-note__icons"><span></span><span></span><span></span></span>
      </div>
      <div class="web-link"><span class="web-link__dot"></span>www.examplesocial.com/WhistlingPines</div>
    </div>

    <div class="bone-band bone-band--bottom" role="img" aria-label="Repeating row of black bones along the bottom edge"></div>
  </main>
</body>
</html>
```